Corporate identity and pre-opening design for a brand new Casino

Dear designers!

We need a design for the pre-opening ad campaign of our brand new casino called "Velvorn Casino" and planned to open soon.
It is situated in "Merisk Lodge Tarvena" – a 4-star luxury and business hotel, located in the city of Plovdiv, Bulgaria.
Our vision of the project is bold, but stylish and elegant. We desire to see uniqueness by all means.
Our slogan is “So many ways to have fun”.
We need a design for our ad campaign for ex. billbord 8m x 4m. We expect your elegant and creative designs. We are trying to avoid the conventional, but at the same time we do not want to be too extravagant.

Thank you and good luck!

Requirements
Should not have
• dices

```html
<!DOCTYPE html>
<html lang="en">
<head>
<meta charset="utf-8">
<title>Velvorn Casino – Identity Stationery</title>
<link href="https://fonts.googleapis.com/css2?family=PT+Serif:ital,wght@0,400;1,400&family=Arimo:wght@400;700&display=swap" rel="stylesheet">
<style>
  :root {
    --brand-red: #a51c26;
    --brand-red-light: #b7222d;
    --brand-red-dark: #921620;
    --swirl-red: #bd2630;
    --blush: #e2a8ad;
    --paper: #ffffff;
    --ink: #1e1e1e;
    --backdrop: #c98e52;
    --label: #1a1a1a;
    --shadow: 2px 2px 3px rgba(0,0,0,0.35);
  }
  * { box-sizing: border-box; margin: 0; padding: 0; }
  html, body { width: 1200px; height: 960px; overflow: hidden; }
  body { background: var(--backdrop); font-family: "PT Serif", serif; color: var(--ink); }
  .stage { position: relative; width: 1200px; height: 960px; overflow: hidden; }

  .item-label { position: absolute; font-family: "Arimo", sans-serif; font-size: 6.5px; color: var(--label); }
  .item-label--large { font-size: 10px; }

  .sheet { position: absolute; background: var(--paper); box-shadow: var(--shadow); overflow: hidden; }
  .sheet--red { background: radial-gradient(ellipse at 50% 55%, var(--brand-red-light), var(--brand-red-dark) 80%); color: var(--paper); }

  .brand-name { position: absolute; font-family: "PT Serif", serif; font-weight: 400; text-transform: uppercase; letter-spacing: 0.03em; line-height: 1.05; text-align: center; }
  .brand-name span { display: block; }
  .brand-name--dark { color: var(--ink); }
  .brand-name--red { color: var(--brand-red); }
  .brand-name--light { color: var(--paper); }

  .contact-block { position: absolute; border-left: 0.6px solid var(--ink); padding-left: 6px; font-size: 4.8px; line-height: 1.25; }

  .swirl-zone { position: absolute; }
  .swirl-zone--red { background: radial-gradient(ellipse at center, rgba(205,45,55,0.75) 0%, rgba(205,45,55,0.35) 45%, rgba(205,45,55,0) 72%); }
  .swirl-zone--blush { background: radial-gradient(ellipse at center, rgba(226,168,173,0.9) 0%, rgba(226,168,173,0.45) 45%, rgba(226,168,173,0) 72%); }

  /* folder */
  .folder { left: 28px; top: 52px; width: 339px; height: 479px; }
  .folder__name { left: 0; width: 100%; top: 248px; font-size: 17.5px; }
  .folder__slogan { position: absolute; top: 303px; width: 100%; text-align: center; font-style: italic; font-size: 11.5px; }

  /* letterhead */
  .letterhead { left: 407px; top: 52px; width: 338px; height: 479px; }
  .letterhead__name { left: 22px; top: 47px; width: 60px; font-size: 7.6px; }
  .letterhead .contact-block { left: 32px; top: 73px; height: 25px; }
  .letterhead__body { position: absolute; left: 83px; top: 109px; width: 173px; font-size: 5.1px; line-height: 1.45; text-align: justify; }
  .letterhead__body p + p { margin-top: 7px; }
  .letterhead__web { position: absolute; left: 26px; top: 446px; font-family: "Arimo", sans-serif; font-weight: 700; font-size: 7px; color: var(--brand-red); }

  /* envelope */
  .envelope { left: 781px; top: 53px; width: 355px; height: 177px; }
  .envelope__name { left: 10px; top: 33px; width: 44px; font-size: 5.4px; }
  .envelope .contact-block { left: 56px; top: 14px; height: 30px; }
  .envelope__address { position: absolute; left: 217px; top: 110px; font-size: 5px; line-height: 1.4; }
  .envelope__address p + p { margin-top: 13px; }

  /* business card */
  .card-front { left: 793px; top: 288px; width: 137px; height: 89px; }
  .card-front__name { left: 22px; top: 13px; font-size: 3.8px; text-align: left; }
  .card-front .contact-block { left: 81px; top: 11px; height: 30px; }
  .card-front__links { position: absolute; left: 11px; top: 71px; display: flex; gap: 11px; font-family: "Arimo", sans-serif; font-weight: 700; font-size: 3.8px; color: var(--brand-red); align-items: center; }
  .card-front__links svg { vertical-align: middle; margin-right: 2px; }
  .card-back { left: 944px; top: 288px; width: 137px; height: 89px; }
  .card-back__name { left: 0; width: 100%; top: 51px; font-size: 9px; }

  /* memo cube */
  .memo { left: 790px; top: 448px; width: 131px; height: 132px; }
  .memo__name { left: 6px; top: 27px; width: 36px; font-size: 4.8px; }

  /* napkins */
  .napkin { position: absolute; left: 956px; width: 197px; box-shadow: var(--shadow); }
  .napkin--light { top: 455px; height: 197px; background: linear-gradient(135deg, #f6dfe1, #efc9cc 50%, #f6dfe1); }
  .napkin--dark { top: 675px; height: 198px; background: linear-gradient(135deg, #b93a43, #c24a52 50%, #b93a43); }

  /* bill holder and matchbox */
  .bill-holder { left: 515px; top: 580px; width: 230px; height: 338px; }
  .bill-holder__name { left: 0; width: 100%; top: 150px; font-size: 12px; }
  .matchbox { left: 406px; top: 737px; width: 54px; height: 97px; }
  .matchbox__name { left: 0; width: 100%; top: 42px; font-size: 6px; }

  /* promotional objects */
  .pencil { position: absolute; left: 339px; top: 572px; width: 10px; height: 170px; box-shadow: var(--shadow); }
  .pencil__tip { position: absolute; top: 0; left: 0; width: 0; height: 0; border-left: 5px solid transparent; border-right: 5px solid transparent; border-bottom: 22px solid #d9b48a; }
  .pencil__lead { position: absolute; top: 0; left: 3.5px; width: 0; height: 0; border-left: 1.5px solid transparent; border-right: 1.5px solid transparent; border-bottom: 6px solid #444; }
  .pencil__body { position: absolute; top: 22px; left: 0; width: 10px; height: 148px; background: var(--paper); }
  .pen { position: absolute; left: 362px; top: 572px; width: 12px; height: 170px; }
  .pen__tip { position: absolute; top: 0; left: 2px; width: 0; height: 0; border-left: 4px solid transparent; border-right: 4px solid transparent; border-bottom: 14px solid #222; }
  .pen__body { position: absolute; top: 14px; left: 0; width: 12px; height: 152px; border-radius: 3px; background: linear-gradient(90deg, var(--brand-red-dark), var(--brand-red-light), var(--brand-red-dark)); box-shadow: var(--shadow); }
  .pen__clip { position: absolute; top: 100px; left: -1px; width: 3px; height: 36px; background: #cfcfcf; border-radius: 1px; }
  .pen__end { position: absolute; bottom: 0; left: 1px; width: 10px; height: 6px; background: #d8d8d8; border-radius: 0 0 2px 2px; }
  .object-mark { position: absolute; font-family: "PT Serif", serif; text-transform: uppercase; font-size: 3.2px; white-space: nowrap; transform: rotate(-90deg); transform-origin: left top; }
  .lighter { position: absolute; left: 441px; top: 599px; width: 26px; height: 91px; }
  .lighter__cap { position: absolute; top: 0; left: 3px; width: 20px; height: 12px; background: #3a3a3a; border-radius: 2px 2px 0 0; }
  .lighter__body { position: absolute; top: 12px; left: 0; width: 26px; height: 79px; background: linear-gradient(90deg, var(--brand-red-dark), var(--brand-red-light), var(--brand-red-dark)); border-radius: 2px; box-shadow: var(--shadow); overflow: hidden; }
  .lighter__name { left: 0; width: 100%; top: 66px; font-size: 3.2px; }
</style>
</head>
<body>
<main class="stage">

  <span class="item-label" style="left:32px;top:24px">folder</span>
  <span class="item-label" style="left:410px;top:24px">letterhead</span>
  <span class="item-label" style="left:791px;top:24px">envelope</span>
  <span class="item-label" style="left:791px;top:271px">card</span>
  <span class="item-label" style="left:791px;top:432px">memo cube</span>
  <span class="item-label item-label--large" style="left:958px;top:431px">Napkin</span>
  <span class="item-label" style="left:517px;top:557px">bill holder</span>
  <span class="item-label" style="left:406px;top:724px">matchbox</span>

  <section class="sheet sheet--red folder">
    <div class="swirl-zone swirl-zone--red" role="img" aria-label="Large faint swirl ornament, upper right" style="left:120px;top:-60px;width:280px;height:260px"></div>
    <div class="swirl-zone swirl-zone--red" role="img" aria-label="Large faint swirl ornament, lower left" style="left:-60px;top:310px;width:240px;height:220px"></div>
    <div class="brand-name brand-name--light folder__name"><span>Velvorn</span><span>Casino</span></div>
    <p class="folder__slogan">So many ways to have fun</p>
  </section>

  <section class="sheet letterhead">
    <div class="brand-name brand-name--dark letterhead__name"><span>Velvorn</span><span>Casino</span></div>
    <div class="contact-block">Contact 2<br>Details 22<br>555 01846<br>55504127</div>
    <div class="letterhead__body">
      <p>Lorem ipsum dolor sit amet, consectetur adipiscing elit. Integer pharetra scelerisque ullamcorper. Proin condimentum eget quam in mattis. Sed ac mi venenatis, mollis dolor nec, pellentesque augue. Integer sed scelerisque enim, sed molestie neque. Etiam quis vestibulum sapien, vel facilisis magna. Nunc eget viverra dui. Maecenas gravida tortor et nibh convallis, et lobortis sapien vehicula.</p>
      <p>Mauris aliquam, nulla ut eleifend condimentum, lacus orci semper neque, eget egestas purus dolor in turpis. Mauris sed massa non sapien rutrum interdum. Donec vitae tellus ut augue cursus sagittis. Nulla a libero eu enim tristique accumsan euismod eget tellus. Vestibulum et volutpat elit, vitae tempus dolor. In suscipit arcu et dui luctus, ut pulvinar risus ornare. Aliquam sit amet feugiat mi, et aliquam velit.</p>
      <p>Suspendisse lacinia nunc et pulvinar mattis. In accumsan magna eget consectetur scelerisque. Suspendisse vitae enim eget urna pharetra vestibulum id eget tellus. Morbi eu mi a felis semper viverra. Mauris mattis efficitur vulputate. Quisque at pellentesque libero, ac elementum elit. Phasellus sodales mattis neque vitae faucibus. Duis mattis molestie est, ut auctor odio luctus quis. Sed ultricies ipsum vel ante varius, a dapibus tortor semper. Suspendisse laoreet velit lobortis tincidunt vulputate. Aenean diam mauris, ultrices quis cursus vitae, facilisis quis libero. Sed non lorem est.</p>
    </div>
    <div class="swirl-zone swirl-zone--blush" role="img" aria-label="Blush swirl ornament, lower right corner" style="left:140px;top:300px;width:240px;height:220px"></div>
    <div class="letterhead__web">www.velvorncasino.com</div>
  </section>

  <section class="sheet envelope">
    <div class="brand-name brand-name--dark envelope__name"><span>Velvorn</span><span>Casino</span></div>
    <div class="contact-block">Contact 2<br>Details 22<br>555 01846<br>55504127</div>
    <div class="swirl-zone swirl-zone--blush" role="img" aria-label="Blush swirl ornament, lower left corner" style="left:-30px;top:70px;width:150px;height:130px"></div>
    <div class="envelope__address">
      <p>Lorem ipsum dolor sit amet, consecte-<br>tur adipiscing elit.</p>
      <p>Lorem ipsum dolor</p>
    </div>
  </section>

  <section class="sheet card-front">
    <div class="brand-name brand-name--red card-front__name"><span>Velvorn</span><span>Casino</span></div>
    <div class="contact-block">Contact 2<br>Details 22<br>555 01846<br>55504127</div>
    <div class="card-front__links">
      <span><svg width="4" height="4" viewBox="0 0 10 10"><path d="M1 1 L9 5 L5 6 L4 9 Z" fill="#1e1e1e"/></svg>www.velvorncasino.com</span>
      <span><svg width="5" height="4" viewBox="0 0 12 9"><rect x="0.5" y="0.5" width="11" height="8" fill="none" stroke="#1e1e1e"/><path d="M0.5 0.5 L6 5 L11.5 0.5" fill="none" stroke="#1e1e1e"/></svg>hello@velvorncasino.com</span>
    </div>
  </section>

  <section class="sheet sheet--red card-back">
    <div class="brand-name brand-name--light card-back__name"><span>Velvorn</span><span>Casino</span></div>
  </section>

  <section class="sheet memo">
    <div class="brand-name brand-name--red memo__name"><span>Velvorn</span><span>Casino</span></div>
    <div class="swirl-zone swirl-zone--blush" role="img" aria-label="Blush swirl ornament, lower right corner" style="left:65px;top:65px;width:90px;height:90px"></div>
  </section>

  <div class="napkin napkin--light" role="img" aria-label="White napkin with repeating red brand pattern"></div>
  <div class="napkin napkin--dark" role="img" aria-label="Red napkin with repeating white brand pattern"></div>

  <section class="sheet bill-holder">
    <div class="brand-name brand-name--red bill-holder__name"><span>Velvorn</span><span>Casino</span></div>
  </section>

  <section class="sheet sheet--red matchbox">
    <div class="brand-name brand-name--light matchbox__name"><span>Velvorn</span><span>Casino</span></div>
  </section>

  <div class="pencil" role="img" aria-label="Branded white pencil">
    <div class="pencil__tip"></div>
    <div class="pencil__lead"></div>
    <div class="pencil__body">
      <span class="object-mark brand-name--red" style="left:3px;top:34px">Velvorn Casino</span>
    </div>
  </div>

  <div class="pen" role="img" aria-label="Branded red pen">
    <div class="pen__tip"></div>
    <div class="pen__body">
      <span class="object-mark brand-name--light" style="left:4px;top:34px">Velvorn Casino</span>
      <div class="pen__end"></div>
    </div>
    <div class="pen__clip"></div>
  </div>

  <div class="lighter" role="img" aria-label="Branded red lighter">
    <div class="lighter__cap"></div>
    <div class="lighter__body">
      <div class="swirl-zone swirl-zone--red" style="left:-10px;top:0;width:46px;height:60px"></div>
      <div class="brand-name brand-name--light lighter__name"><span>Velvorn</span><span>Casino</span></div>
    </div>
  </div>

</main>
</body>
</html>
```